Real Estate 2015 sold listings postcard

Real estate. I want one side to list 2015 sales. Mailing side with additional information. I am including a "concept" but it needs to be professionalized... Feel free to change color, fonts, layout, add watermark, whatever you think will work. Text on backside may be tweaked. I do want postcards addressed. How do i send mailing list or does Quorra Mail do that part?

NOTE: Postcard should be 8.5 x 5.5 inches.

postcard should be 8.5" x 5.5" size

Target Market(s)

Home owners who may want to sell

Industry/Entity Type

Real Estate Agent

Requirements
Must have
• The sold information and contact oinformation I have provided
Nice to have
• Watermark with my initials

```html
<!DOCTYPE html>
<html lang="en">
<head>
<meta charset="utf-8">
<title>2015 Sales Postcard – Harbor Crest Realty</title>
<link href="https://fonts.googleapis.com/css2?family=Oswald:wght@400;500;700&family=Open+Sans:wght@300;400;600&family=Satisfy&display=swap" rel="stylesheet">
<style>
:root{
  --backdrop:#756657;
  --paper:#ffffff;
  --gold:#d6a117;
  --ink:#111111;
  --row-alt:#e6e6e6;
  --blue-top:#1d5fae;
  --blue-bottom:#0b2f66;
  --stamp:#bfc0c2;
  --line:#bdbdbd;
}
*{box-sizing:border-box;margin:0;padding:0}
html,body{width:952px;height:1200px;overflow:hidden;background:var(--backdrop)}
body{position:relative;font-family:"Open Sans",Arial,sans-serif;color:var(--ink)}
.card{position:absolute;left:93px;width:762px;height:493px;background:var(--paper);box-shadow:3px 4px 6px rgba(0,0,0,.35);overflow:hidden}
.card--front{top:83px}
.card--back{top:617px}

/* brand lockup */
.brand{position:absolute;display:flex;align-items:center;gap:8px}
.brand__mark{width:18px;height:18px;background:var(--gold)}
.brand__name{font-family:"Oswald",sans-serif;font-weight:500;font-size:23px;letter-spacing:.5px;color:var(--ink);white-space:nowrap}
.card--front .brand{left:18px;top:38px}
.card--back .brand{left:452px;top:78px}

/* headline bar */
.title-bar{position:absolute;left:225px;top:36px;width:432px;height:42px;background:var(--gold);color:#fff;font-family:"Oswald",sans-serif;font-weight:700;font-size:27px;line-height:42px;text-align:center;letter-spacing:.3px;white-space:nowrap}
.title-sold{position:absolute;left:660px;top:36px;width:84px;height:42px;background:var(--gold);color:var(--ink);font-family:"Oswald",sans-serif;font-weight:400;font-size:27px;line-height:42px;text-align:center}
.title-rule{position:absolute;left:225px;top:81px;width:519px;height:9px;background:var(--ink)}

/* sales table */
.sales{position:absolute;left:18px;top:113px;width:727px;border-collapse:collapse;table-layout:fixed;font-size:11.5px}
.sales th{background:var(--ink);color:#fff;font-weight:600;font-size:13px;height:22px;text-align:center;border-left:1px solid #fff}
.sales th:first-child{text-align:left;padding-left:10px;border-left:none}
.sales td{height:18px;text-align:center;border-left:1px solid var(--ink);white-space:nowrap}
.sales td:first-child{text-align:left;padding-left:10px;border-left:none}
.sales td.lot-b{border-left:none}
.sales tbody tr:first-child td{padding-top:4px;height:22px}
.sales tbody tr:nth-child(even) td{background:var(--row-alt)}

/* contact footer */
.contact-bar{position:absolute;left:18px;top:439px;width:727px;height:46px;background:var(--gold);color:#fff}
.contact-bar > *{position:absolute;white-space:nowrap}
.contact-bar__name{left:12px;top:2px;font-family:"Oswald",sans-serif;font-weight:500;font-size:19px}
.contact-bar__role{left:12px;top:27px;font-size:11.5px;font-weight:300}
.contact-bar__divider{top:6px;width:1px;height:34px;background:rgba(255,255,255,.7)}
.contact-bar__email{left:160px;top:11px;font-size:16.5px;font-weight:300}
.contact-bar__web{left:391px;top:10px;font-size:17px;font-weight:600}
.contact-bar__note{left:576px;top:7px;width:148px;font-size:7px;line-height:10.5px;white-space:normal}

/* back – message panel */
.message{position:absolute;left:0;top:0;width:435px;height:493px;background:var(--gold);color:#fff}
.message__headline{position:absolute;left:23px;top:18px;width:400px;font-family:"Oswald",sans-serif;font-weight:700;font-size:27px;line-height:32px}
.message__body{position:absolute;left:23px;width:394px;font-size:10.8px;line-height:16.2px;font-weight:400;text-align:justify}
.message__body--one{top:86px}
.message__body--two{top:180px}
.message__tip{position:absolute;left:24px;top:284px;font-family:"Oswald",sans-serif;font-weight:500;font-size:15.5px;line-height:20px;color:#2a2a2a;white-space:nowrap}

.offer{position:absolute;left:25px;top:310px;width:393px;height:190px;background:linear-gradient(var(--blue-top),var(--blue-bottom));border:1px dashed #9db8e0;border-radius:5px 5px 0 0}
.offer__title{position:absolute;left:0;top:3px;width:100%;text-align:center;font-family:"Oswald",sans-serif;font-weight:700;font-size:24px;color:#fff;letter-spacing:.3px}
.offer__panel{position:absolute;left:4px;top:41px;width:383px;height:150px;background:var(--ink);border-radius:4px 4px 0 0}
.offer__script{position:absolute;left:10px;top:4px;font-family:"Satisfy",cursive;color:#fff;font-size:18px;line-height:31px;white-space:nowrap}
.offer__script .accent{color:var(--gold);font-size:22px}
.offer__divider{position:absolute;left:112px;top:18px;width:1px;height:110px;background:#fff}
.agent{position:absolute;left:124px;top:6px;color:#fff;white-space:nowrap}
.agent__name{font-family:"Oswald",sans-serif;font-weight:500;font-size:20px;line-height:26px}
.agent__role{font-size:14px;line-height:20px;margin-top:2px}
.agent__license{font-size:14px;line-height:20px;margin-top:11px}
.agent__phone{font-family:"Oswald",sans-serif;font-weight:500;font-size:23px;margin-top:9px}
.agent__photo{position:absolute;left:274px;top:10px;width:99px;height:140px;border-radius:6px 6px 0 0;background:linear-gradient(180deg,#7a5a3a 0%,#c9967a 40%,#c92a33 75%,#a11b25 100%)}

/* back – address side */
.stamp{position:absolute;left:648px;top:15px;width:93px;height:112px;background:var(--stamp)}
.address-line{position:absolute;left:476px;width:265px;height:1px;background:var(--line)}
</style>
</head>
<body>

<section class="card card--front">
  <div class="brand"><span class="brand__mark"></span><span class="brand__name">HARBOR CREST</span></div>
  <div class="title-bar">2015 SALES IN YOUR NEIGHBORHOOD</div>
  <div class="title-sold">SOLD</div>
  <div class="title-rule"></div>

  <table class="sales">
    <colgroup>
      <col style="width:141px"><col style="width:43px"><col style="width:54px"><col style="width:54px">
      <col style="width:70px"><col style="width:70px"><col style="width:85px"><col style="width:86px">
      <col style="width:70px"><col style="width:54px">
    </colgroup>
    <thead>
      <tr><th>Address</th><th>BR</th><th>BA</th><th>Sq Ft</th><th colspan="2">Lot Size</th><th>List Price</th><th>Sale Price</th><th>$/Sq. Ft</th><th>DOM</th></tr>
    </thead>
    <tbody>
      <tr><td>387 Alder PL*</td><td>3</td><td>3 1/2</td><td></td><td>2588</td><td class="lot-b">9239</td><td>3088000</td><td>3,100,000</td><td>1198</td><td>9</td></tr>
      <tr><td>3657 Birch ST</td><td>4</td><td>3</td><td></td><td>2228</td><td class="lot-b">6147</td><td>2998000</td><td>3000000</td><td>1346</td><td>23</td></tr>
      <tr><td>261 Brookview DR</td><td>4</td><td>3</td><td></td><td>2185</td><td class="lot-b">7040</td><td>2500000</td><td>2925000</td><td>1,339</td><td>9</td></tr>
      <tr><td>437 Fennel AVE*</td><td>4</td><td>2</td><td></td><td>1611</td><td class="lot-b">13,237</td><td>2498000</td><td>2610000</td><td>1620</td><td>8</td></tr>
      <tr><td>4123 Dale AVE*</td><td>4</td><td>2</td><td></td><td>2227</td><td class="lot-b">8700</td><td>2295000</td><td>2595000</td><td>1165</td><td>8</td></tr>
      <tr><td>76 Ridgeway CIR *</td><td>3</td><td>2</td><td></td><td>1364</td><td class="lot-b">5917</td><td>1788000</td><td>2525000</td><td>1851</td><td>8</td></tr>
      <tr><td>3665 Marina CIR</td><td>4</td><td>2</td><td></td><td>1646</td><td class="lot-b">6404</td><td>2500000</td><td>2475000</td><td>1504</td><td>18</td></tr>
      <tr><td>410 Aspen PL *</td><td>3</td><td>2</td><td></td><td>1674</td><td class="lot-b">11200</td><td>2498000</td><td>2450000</td><td>1464</td><td>16</td></tr>
      <tr><td>291 Brookview DR*</td><td>4</td><td>2</td><td></td><td>1690</td><td class="lot-b">8178</td><td>2199000</td><td>2400000</td><td>1420</td><td>7</td></tr>
      <tr><td>303 Brookview DR.</td><td>3</td><td>2</td><td></td><td>1674</td><td class="lot-b">8538</td><td>2200000</td><td>2260000</td><td>1350</td><td>97</td></tr>
      <tr><td>93 Ridgeway CIR</td><td>3</td><td>2</td><td></td><td>1243</td><td class="lot-b">6080</td><td>1488000</td><td>2250000</td><td>1810</td><td>7</td></tr>
      <tr><td>3702 Carver CIR *</td><td>4</td><td>2</td><td></td><td>1333</td><td class="lot-b">6493</td><td>1895000</td><td>2227500</td><td>1671</td><td>6</td></tr>
      <tr><td>372 Parkline DR *</td><td>3</td><td>2</td><td></td><td>1740</td><td class="lot-b">6324</td><td>2200000</td><td>2180000</td><td>1,253</td><td>12</td></tr>
      <tr><td>3647 Birch ST</td><td>4</td><td>2</td><td></td><td>1474</td><td class="lot-b">6111</td><td>1799900</td><td>2115000</td><td>1,435</td><td>17</td></tr>
      <tr><td>60 Ridgeway Cir</td><td>4</td><td>2</td><td></td><td>1456</td><td class="lot-b">6111</td><td>1788000</td><td>2000000</td><td>1374</td><td>11</td></tr>
      <tr><td>252 Fairmont CT</td><td>3</td><td>2</td><td></td><td>1428</td><td class="lot-b">10,624</td><td>1,950,000</td><td>2,100,000</td><td>1471</td><td>20</td></tr>
    </tbody>
  </table>

  <div class="contact-bar">
    <div class="contact-bar__name">Dana Whitlow</div>
    <div class="contact-bar__role">Relocation Specialist</div>
    <div class="contact-bar__divider" style="left:143px"></div>
    <div class="contact-bar__email">email: dana@hcrealty.com</div>
    <div class="contact-bar__divider" style="left:372px"></div>
    <div class="contact-bar__web">www.dwhitlow.com</div>
    <div class="contact-bar__divider" style="left:565px"></div>
    <div class="contact-bar__note">* indicates Harbor Crest Realty listing or sale. This information is deemed reliable, but not verified or guaranteed.</div>
  </div>
</section>

<section class="card card--back">
  <div class="message">
    <h1 class="message__headline">Our Listings are advertised locally and in 40 countries!!</h1>
    <p class="message__body message__body--one">Our market continues to be strong, which reflects both our vibrant and growing local economy and our seemingly chronic shortage of inventory. As long as those conditions continue, our market values will remain high. That is good news to sellers who may want to down-size or move to a different area for a new job, or maybe to be closer to family.</p>
    <p class="message__body message__body--two">I am an Harbor Crest Realty certified Relocation Specialist, and, as such, I can connect you with experienced and professional real estate agent anywhere in the country and in most countries around the world. We can co-ordinate your transactions at both ends, making your transition as seamless as possible. If you are planning a move, across the street or across the county, call me now for a confidential consultation.</p>
    <p class="message__tip">Traditionally, Feb. through April are the best months to sell</p>

    <div class="offer">
      <div class="offer__title">MOST OFFERS,&nbsp; HIGHEST PRICES</div>
      <div class="offer__panel">
        <div class="offer__script">Don't Wait.<br><span class="accent">Call Now</span><br>for a Private<br>Consultation!</div>
        <div class="offer__divider"></div>
        <div class="agent">
          <div class="agent__name">DANA WHITLOW</div>
          <div class="agent__role">Relocation Specialist</div>
          <div class="agent__license">License: #01234567</div>
          <div class="agent__phone">650-555-0148</div>
        </div>
        <div class="agent__photo" role="img" aria-label="Portrait photo of the agent"></div>
      </div>
    </div>
  </div>

  <div class="brand"><span class="brand__mark"></span><span class="brand__name">HARBOR CREST</span></div>
  <div class="stamp"></div>
  <div class="address-line" style="top:237px"></div>
  <div class="address-line" style="top:272px"></div>
  <div class="address-line" style="top:307px"></div>
  <div class="address-line" style="top:342px"></div>
  <div class="address-line" style="top:378px"></div>
</section>

</body>
</html>
```